Lanternfield Ministries Project Harvestline

I have a pop up display for inside tradeshows I would like for you to design. Here are the dimensions

pop up stand: 33(left side)+300+33cm(right side)

prodium: 1.04*2.2m

X stand: 60*160cm
I want to use the grayscale color wheel.
I want the backwall, xframes, and prodium to flow cohesively. I give you creative control on this project. Afterwards we will collaborate on the details. I want light gray from top gradually fading down to black which should be on the bottom.

Target Market(s)

Men and women from ages 16-59 yrs of age

Industry/Entity Type

Religious/ministry

Font styles to use
Serif

Colors

Designer to choose only greyscale colors for use in the design.

Requirements
Should not have
• N/a

```html
<!DOCTYPE html>
<html lang="en">
<head>
<meta charset="utf-8">
<title>Lanternfield Ministries – Tradeshow Display</title>
<link rel="stylesheet" href="https://fonts.googleapis.com/css2?family=Bebas+Neue&family=Montserrat:wght@400;600;700&display=swap">
<style>
  :root {
    --page: #ffffff;
    --grey-top: #adadad;
    --grey-mid: #555555;
    --black: #111111;
    --ink: #0d0d0d;
    --white: #ffffff;
    --fade: linear-gradient(to bottom, var(--grey-top) 0%, #8a8a8a 25%, var(--grey-mid) 48%, #1e1e1e 72%, var(--black) 100%);
  }
  * { margin: 0; padding: 0; box-sizing: border-box; }
  html, body { width: 720px; height: 1200px; overflow: hidden; background: var(--page); }
  .canvas { position: relative; width: 720px; height: 1200px; }

  .panel { position: absolute; background: var(--fade); overflow: hidden; }

  .brand { position: absolute; left: 0; right: 0; text-align: center; }
  .brand-mark { display: block; margin: 0 auto; background: var(--ink); border-radius: 3px; }
  .brand-name {
    display: block; font-family: "Montserrat", sans-serif; font-weight: 700;
    color: var(--ink); white-space: nowrap; letter-spacing: 0.01em;
  }
  .brand-tagline {
    display: block; font-family: "Montserrat", sans-serif; font-weight: 400;
    color: var(--ink); letter-spacing: 0.25em; white-space: nowrap;
  }

  .headline {
    position: absolute; font-family: "Bebas Neue", sans-serif; color: var(--white);
    line-height: 0.95; letter-spacing: 0.01em;
  }
  .rule { position: absolute; height: 2px; background: var(--white); }
  .pillars {
    position: absolute; list-style: none; font-family: "Montserrat", sans-serif;
    font-weight: 600; color: var(--white); letter-spacing: 0.05em;
  }
  .pillars li::before { content: "• "; }
  .site {
    position: absolute; left: 0; right: 0; text-align: center;
    font-family: "Montserrat", sans-serif; color: var(--white); white-space: nowrap;
  }
  .site b { font-weight: 700; }

  /* X stands */
  .xstand { top: 353px; width: 115px; height: 306px; }
  .xstand.left { left: 38px; }
  .xstand.right { left: 580px; }
  .xstand .brand { top: 13px; }
  .xstand .brand-mark { width: 30px; height: 22px; }
  .xstand .brand-name { font-size: 9.5px; margin-top: 5px; }
  .xstand .brand-tagline { font-size: 3px; margin-top: 2px; }
  .xstand .headline { left: 10px; top: 84px; font-size: 20px; }
  .xstand .rule { left: 10px; top: 128px; width: 18px; height: 1.5px; }
  .xstand .pillars { left: 10px; top: 137px; font-size: 9.6px; line-height: 13.6px; }
  .xstand .site { top: 273px; font-size: 4.6px; font-weight: 700; }

  /* Side returns */
  .return { top: 353px; width: 32px; height: 306px; }
  .return.left { left: 178px; }
  .return.right { left: 515px; }
  .return .site {
    top: 50%; left: 50%; right: auto; font-size: 9.5px;
    transform: translate(-50%, -50%) rotate(-90deg); transform-origin: center;
    margin-top: 62px;
  }

  /* Back wall */
  .backwall { left: 217px; top: 353px; width: 292px; height: 306px; }
  .backwall .brand { top: 17px; }
  .backwall .brand-mark { width: 54px; height: 40px; }
  .backwall .brand-name { font-size: 17px; margin-top: 8px; }
  .backwall .brand-tagline { font-size: 4.6px; margin-top: 3px; }
  .backwall .headline { left: 29px; top: 128px; font-size: 31px; }
  .backwall .rule { left: 29px; top: 160px; width: 42px; }
  .backwall .pillars { top: 168px; font-size: 12.4px; line-height: 15.5px; }
  .backwall .pillars.first { left: 29px; }
  .backwall .pillars.second { left: 141px; }
  .backwall .site { top: 255px; font-size: 9.5px; }

  /* Podium wrap */
  .podium { left: 217px; top: 682px; width: 289px; height: 164px; }
  .podium .fold { position: absolute; top: 0; bottom: 0; width: 1px; background: rgba(255,255,255,0.25); }
  .podium .fold.a { left: 71px; }
  .podium .fold.b { left: 219px; }
  .podium .brand { top: 37px; }
  .podium .brand-mark { width: 38px; height: 28px; }
  .podium .brand-name { font-size: 11.5px; margin-top: 6px; }
  .podium .brand-tagline { font-size: 3.4px; margin-top: 2px; }
  .podium .site { top: 126px; font-size: 5.6px; font-weight: 700; }
</style>
</head>
<body>
<main class="canvas">

  <section class="panel xstand left" aria-label="X stand banner">
    <div class="brand">
      <span class="brand-mark"></span>
      <span class="brand-name">Lanternfield Ministries</span>
      <span class="brand-tagline">A HAND OUT IS A HAND UP</span>
    </div>
    <h2 class="headline">A Hand Out Is<br>A Hand Up</h2>
    <div class="rule"></div>
    <ul class="pillars"><li>FAITH</li><li>COMMUNITY</li><li>SOBRIETY</li><li>SUSTAINABLE</li></ul>
    <p class="site">www.lanternfieldministries.org</p>
  </section>

  <section class="panel return left" aria-label="Back wall left return">
    <p class="site">www.<b>lanternfieldministries</b>.org</p>
  </section>

  <section class="panel backwall" aria-label="Pop up back wall">
    <div class="brand">
      <span class="brand-mark"></span>
      <span class="brand-name">Lanternfield Ministries</span>
      <span class="brand-tagline">A HAND OUT IS A HAND UP</span>
    </div>
    <h1 class="headline">A Hand Out Is A Hand Up</h1>
    <div class="rule"></div>
    <ul class="pillars first"><li>FAITH</li><li>COMMUNITY</li></ul>
    <ul class="pillars second"><li>SOBRIETY</li><li>SUSTAINABLE</li></ul>
    <p class="site">www.<b>lanternfieldministries</b>.org</p>
  </section>

  <section class="panel return right" aria-label="Back wall right return">
    <p class="site">www.<b>lanternfieldministries</b>.org</p>
  </section>

  <section class="panel xstand right" aria-label="X stand banner">
    <div class="brand">
      <span class="brand-mark"></span>
      <span class="brand-name">Lanternfield Ministries</span>
      <span class="brand-tagline">A HAND OUT IS A HAND UP</span>
    </div>
    <h2 class="headline">A Hand Out Is<br>A Hand Up</h2>
    <div class="rule"></div>
    <ul class="pillars"><li>FAITH</li><li>COMMUNITY</li><li>SOBRIETY</li><li>SUSTAINABLE</li></ul>
    <p class="site">www.lanternfieldministries.org</p>
  </section>

  <section class="panel podium" aria-label="Podium wrap">
    <div class="fold a"></div>
    <div class="fold b"></div>
    <div class="brand">
      <span class="brand-mark"></span>
      <span class="brand-name">Lanternfield Ministries</span>
      <span class="brand-tagline">A HAND OUT IS A HAND UP</span>
    </div>
    <p class="site">www.lanternfieldministries.org</p>
  </section>

</main>
</body>
</html>
```